plumbing fleet vehicles

I want to create a fleet of vehicles wraps for multiple types of company vehicles, brask vesta, K730, Dorin 300 service truck, Brask ambler van, Dorin 300 box truck, Dorin Kestrano 2022, and box trailor. I want to use the example color blocking and witty pun for our business with a simple play on our logos, brand colors, brand mark. make is stand out, simple, edgy, contrast, and witty

```html
<!DOCTYPE html>
<html lang="en">
<head>
<meta charset="utf-8">
<title>Clearway Fleet Wraps</title>
<link href="https://fonts.googleapis.com/css2?family=Barlow+Condensed:wght@600;700&family=Barlow:wght@500;600&display=swap" rel="stylesheet">
<style>
:root{
  --navy:#14213f;
  --orange:#ec8112;
  --white:#ffffff;
  --paper:#f4f4f2;
  --label:#4a4a4a;
}
*{box-sizing:border-box;margin:0;padding:0}
html,body{width:1200px;height:800px;overflow:hidden;background:var(--paper)}
.fleet{position:relative;width:1200px;height:800px;font-family:"Barlow",sans-serif}
.vehicle-label{position:absolute;font:500 11px "Barlow",sans-serif;color:var(--label);letter-spacing:.2px;white-space:nowrap;z-index:2}
.wrap{position:absolute;background:var(--white);overflow:hidden;box-shadow:0 6px 14px rgba(0,0,0,.12);border-radius:6px}
.wrap-orange{position:absolute;top:0;right:0;height:100%;background:var(--orange);
  clip-path:polygon(12% 0,100% 0,100% 100%,0 100%);padding-left:9%;display:flex;flex-direction:column;justify-content:center}
.wrap-orange.square{clip-path:none;padding-left:4%}
.wrap-navy{position:absolute;left:0;bottom:0;width:100%;background:var(--navy);display:flex;align-items:center;justify-content:flex-end;padding-right:6%}
.brand{position:absolute;display:flex;align-items:center;gap:8px;color:var(--navy);font-family:"Barlow Condensed",sans-serif;font-weight:700;line-height:1;white-space:nowrap}
.brand-dot{width:.45em;height:.45em;border-radius:50%;background:var(--orange);flex:none}
.tagline{font-family:"Barlow Condensed",sans-serif;font-weight:700;color:var(--navy);line-height:1.05;text-transform:uppercase}
.rule{height:1px;background:rgba(255,255,255,.75);margin:6px 0;width:85%}
.phone{font-weight:600;color:var(--white);line-height:1.2}
.web{font-weight:600;color:var(--white);text-transform:uppercase;line-height:1.2}
.band-text{font-family:"Barlow",sans-serif;font-weight:600;color:var(--white);font-size:13px;letter-spacing:.3px}
</style>
</head>
<body>
<main class="fleet">

  <span class="vehicle-label" style="left:20px;top:16px">BRASK VESTA</span>
  <section class="wrap" style="left:50px;top:40px;width:460px;height:120px">
    <div class="brand" style="left:24px;top:44px;font-size:30px"><span class="brand-dot"></span>CLEARWAY</div>
    <div class="wrap-orange" style="width:48%;height:86%">
      <p class="tagline" style="font-size:15px">Leaks don't wait.<br>Neither do we.</p>
      <p class="phone" style="font-size:11px;margin-top:8px">555.014.2287</p>
      <p class="web" style="font-size:7px">clearwayplumber.com</p>
    </div>
    <div class="wrap-navy" style="height:14%"></div>
  </section>

  <span class="vehicle-label" style="left:578px;top:16px">BRASK K730</span>
  <section class="wrap" style="left:590px;top:40px;width:580px;height:130px">
    <div class="brand" style="left:150px;top:48px;font-size:32px"><span class="brand-dot"></span>CLEARWAY</div>
    <div class="wrap-orange" style="width:46%;height:84%">
      <p class="tagline" style="font-size:16px">Big jobs. Zero drama.</p>
      <p class="phone" style="font-size:12px;margin-top:10px">555.014.2287</p>
      <p class="web" style="font-size:8px">clearwayplumber.com</p>
    </div>
    <div class="wrap-navy" style="height:16%"></div>
  </section>

  <span class="vehicle-label" style="left:20px;top:204px">DORIN 300 SERVICE TRUCK</span>
  <section class="wrap" style="left:40px;top:228px;width:480px;height:128px">
    <div class="brand" style="left:150px;top:46px;font-size:28px"><span class="brand-dot"></span>CLEARWAY</div>
    <div class="wrap-orange square" style="width:32%;height:84%">
      <p class="tagline" style="font-size:13px">Fixed right.<br>First time.</p>
      <p class="phone" style="font-size:10px;margin-top:10px">555.014.2287</p>
      <p class="web" style="font-size:6.5px">clearwayplumber.com</p>
    </div>
    <div class="wrap-navy" style="height:16%"></div>
  </section>

  <span class="vehicle-label" style="left:565px;top:204px">BRASK AMBLER VAN</span>
  <section class="wrap" style="left:565px;top:228px;width:595px;height:150px">
    <div class="brand" style="left:170px;top:56px;font-size:38px"><span class="brand-dot"></span>CLEARWAY</div>
    <div class="wrap-orange" style="width:40%;height:84%;padding-left:11%">
      <p class="tagline" style="font-size:17px">Big show up.<br>Problems don't.</p>
      <div class="rule"></div>
      <p class="phone" style="font-size:11px">555.014.2287</p>
      <p class="web" style="font-size:8px">clearwayplumber.com</p>
    </div>
    <div class="wrap-navy" style="height:16%"></div>
  </section>

  <span class="vehicle-label" style="left:20px;top:404px">DORIN 300 BOX TRUCK</span>
  <section class="wrap" style="left:178px;top:400px;width:360px;height:150px">
    <div class="brand" style="left:16px;top:56px;font-size:30px;gap:6px"><span class="brand-dot"></span>CLEARWAY</div>
    <div class="wrap-orange square" style="width:52%;height:86%;padding-left:5%">
      <p class="tagline" style="font-size:20px">When in doubt,<br>call Clearway.</p>
      <div class="rule"></div>
      <p class="phone" style="font-size:12px">555.014.2287</p>
      <p class="web" style="font-size:8px">clearwayplumber.com</p>
    </div>
    <div class="wrap-navy" style="height:14%"></div>
  </section>

  <span class="vehicle-label" style="left:572px;top:404px">DORIN KESTRANO 2022</span>
  <section class="wrap" style="left:605px;top:428px;width:535px;height:130px">
    <div class="brand" style="left:130px;top:50px;font-size:32px"><span class="brand-dot"></span>CLEARWAY</div>
    <div class="wrap-orange" style="width:45%;height:82%;padding-left:11%">
      <p class="tagline" style="font-size:14px">Plumbing help.<br>One call away.</p>
      <p class="phone" style="font-size:10px;margin-top:8px">555.014.2287</p>
      <p class="web" style="font-size:7px">clearwayplumber.com</p>
    </div>
    <div class="wrap-navy" style="height:18%"></div>
  </section>

  <section class="wrap" style="left:325px;top:585px;width:455px;height:150px;border-radius:3px">
    <div class="brand" style="left:20px;top:40px;font-size:32px;gap:6px"><span class="brand-dot"></span>CLEARWAY</div>
    <div class="wrap-orange square" style="width:59%;height:74%;padding-left:4%">
      <p class="tagline" style="font-size:20px">This is your sign.<br>Call Clearway.</p>
      <div class="rule"></div>
      <p class="phone" style="font-size:13px">555.014.2287</p>
      <p class="web" style="font-size:9px">clearwayplumber.com</p>
    </div>
    <div class="wrap-navy" style="height:26%"><span class="band-text">CLEARWAY CLEARS ALL.</span></div>
  </section>
  <span class="vehicle-label" style="left:500px;top:776px">BOX TRAILER</span>

</main>
</body>
</html>
```